Veloran Dental Development - Business Cards

We are a Dental Development and Management company. We are looking to develop a new business card design. We are business professional but modern. The logo that I have attached is the business colors. You can also check out our website for further detail. www.veloranmgmt-example.com

Target Market(s)

Dental Professionals, Dentists and Office Staff, Marketing Professionals

Industry/Entity Type

Business

Requirements
Must have
• Name - Bartholomew K. Tressing
Title - Marketing Director
Phone - 555-019-4827
Cell - 555-019-4827
Email - Bart.t@veloran-example.com
Address - 2917 W Larkmoor Rd, Mesa, AZ 85209
Web- www.veloran-example.com

Veloran Logo must go on the front. The other logos go on the back as affiliated businesses

Must be editable to enter specific Names, Positions, Phone numbers and email later on. Using Adobe CS5 currently.

```html
<!DOCTYPE html>
<html lang="en">
<head>
<meta charset="utf-8">
<title>Veloran Dental Development – Business Cards</title>
<link href="https://fonts.googleapis.com/css2?family=Crimson+Text:wght@400;600;700&display=swap" rel="stylesheet">
<style>
  :root {
    --navy: #043a5e;
    --olive: #5a6a1f;
    --paper: #fafafa;
    --page: #ffffff;
    --white: #ffffff;
  }
  * { margin: 0; padding: 0; box-sizing: border-box; }
  html, body {
    width: 1200px; height: 900px; overflow: hidden;
    background: var(--page);
    font-family: "Crimson Text", Georgia, serif;
  }
  .canvas { position: relative; width: 1200px; height: 900px; }
  .card {
    position: absolute; left: 403px;
    width: 395px; height: 232px;
    background: var(--paper);
    overflow: hidden;
    box-shadow: 0 6px 22px rgba(0,0,0,0.18);
  }
  .card--front { top: 193px; }
  .card--back { top: 471px; }
  .card__waves { position: absolute; inset: 0; width: 100%; height: 100%; }
  .brand {
    position: absolute; left: 0; right: 0;
    display: flex; align-items: center; justify-content: center; gap: 9px;
  }
  .card--front .brand { top: 40px; }
  .card--back .brand { top: 42px; }
  .brand__dot {
    width: 14px; height: 14px; border-radius: 50%;
    background: var(--olive);
  }
  .brand__name {
    font-weight: 700; font-size: 27px; line-height: 1;
    color: var(--navy); letter-spacing: 0.2px;
  }
  .holder {
    position: absolute; left: 22px; top: 160px;
    color: var(--white); text-align: center; width: 150px;
  }
  .holder__name { font-weight: 700; font-size: 18px; line-height: 1.1; }
  .holder__title { font-size: 8.5px; font-weight: 600; letter-spacing: 0.4px; margin-top: 5px; }
  .contact {
    position: absolute; left: 196px; top: 153px;
    list-style: none; color: var(--white);
    font-size: 10.5px; font-weight: 600; line-height: 18px;
  }
  .website {
    position: absolute; left: 0; right: 0; top: 198px;
    text-align: center; color: var(--white);
    font-weight: 700; font-size: 17px;
  }
</style>
</head>
<body>
<main class="canvas">
  <section class="card card--front" aria-label="Business card front">
    <svg class="card__waves" viewBox="0 0 395 232" preserveAspectRatio="none" aria-hidden="true">
      <path d="M0 111 Q197 138 395 111 L395 232 L0 232 Z" fill="var(--olive)"/>
      <path d="M0 122 Q197 145 395 122 L395 232 L0 232 Z" fill="var(--navy)"/>
    </svg>
    <div class="brand">
      <span class="brand__dot"></span>
      <span class="brand__name">Hearthside Dental Centers</span>
    </div>
    <div class="holder">
      <p class="holder__name">Bartholomew<br>K. Tressing</p>
      <p class="holder__title">MARKETING DIRECTOR</p>
    </div>
    <ul class="contact">
      <li>Phone - 555-019-4827</li>
      <li>Cell - 555-019-4827</li>
      <li>Bart.t@veloran-example.com</li>
      <li>2917 W Larkmoor Rd, Mesa, AZ 85209</li>
    </ul>
  </section>

  <section class="card card--back" aria-label="Business card back">
    <svg class="card__waves" viewBox="0 0 395 235" preserveAspectRatio="none" aria-hidden="true">
      <path d="M0 140 Q197 105 395 140 L395 235 L0 235 Z" fill="var(--olive)"/>
      <path d="M0 152 Q197 115 395 152 L395 235 L0 235 Z" fill="var(--navy)"/>
    </svg>
    <div class="brand">
      <span class="brand__dot"></span>
      <span class="brand__name">Hearthside Dental Centers</span>
    </div>
    <p class="website">www.veloran-example.com</p>
  </section>
</main>
</body>
</html>
```